Driving-coach/trainer who wants to inform about the offer and how I can help people to drive more re

I need a flyer that informs potential customers about my offer.

DL size 210 mm x 99 mm, vertical!

I'm a trainer/coach who helps people to drive a car more relaxed, without fear and more confident.

It's a one to one training. I do train people in their own car. It gets people their freedom back to go where and when they like to go by own car...
Updates

Project Deadline Extended Reason: I would like to extend my project... didn't find the time to give feedback because of unexpected other jobs I had to do.Would be great if you could extend my project around 5 more days. THANKS. Added Wednesday, January 4, 2017

Target Market(s)

People (man an woman) who are afraid of driving a car, or are very stressed while driving....

Industry/Entity Type

Life Coaching

Font styles to use
Sans Serif

Colors
acd136

Requirements
Must have
• Page 1:
• -my offer (see text-pdf)
• -three fotos (see attached files "Pixavine") of people who are satisfied with my offer
• Page 2:
• -advantages in the work with me.
• -contact information
• -and a picture of me (see attached file) next to the contact information or the advantages of my work
• -my logo (see attached file) on Page 1 + 2
• -i like a "clear" and structured layout. "Less is more"

```html
<!DOCTYPE html>
<html lang="de">
<head>
<meta charset="utf-8">
<title>Fahrangst-Bewältigungs-Coach Flyer</title>
<link href="https://fonts.googleapis.com/css2?family=Oswald:wght@500;700&family=Montserrat:wght@300;400;600&display=swap" rel="stylesheet">
<style>
:root{
  --green:#3f9e34;
  --green-bright:#4cab3a;
  --green-dark:#0f3b24;
  --pale:#e9f2e0;
  --pale-2:#f4f8ef;
  --white:#ffffff;
  --ink:#333a33;
  --gap:#ffffff;
}
*{margin:0;padding:0;box-sizing:border-box}
html,body{width:1123px;height:1200px;overflow:hidden;background:var(--gap)}
body{position:relative;font-family:'Montserrat',sans-serif;color:var(--ink)}
.page{position:absolute;top:0;height:1200px;overflow:hidden}
.page--front{left:0;width:551px;background:var(--pale)}
.page--back{left:574px;width:549px;background:linear-gradient(160deg,var(--pale),var(--pale-2))}
.abs{position:absolute}
.display{font-family:'Oswald',sans-serif;font-weight:700;text-transform:uppercase;line-height:.92}
.headline{font-size:72px;letter-spacing:-.5px}
.headline .dark{color:var(--green-dark)}
.headline .light{color:var(--white)}
.kicker{font-family:'Oswald',sans-serif;font-weight:700;font-size:18px;letter-spacing:4px;color:var(--green-dark);text-transform:uppercase}
.questions{list-style:none}
.questions li{position:relative;font-family:'Oswald',sans-serif;font-weight:500;font-size:24px;line-height:1.1;color:var(--white);text-transform:uppercase;padding-left:41px;margin-bottom:12px}
.questions svg{position:absolute;left:0;top:5px}
.callout{font-size:36px;color:var(--green-dark);line-height:1.05}
.situations-title{font-family:'Oswald',sans-serif;font-weight:700;font-size:19px;color:#2a2a2a;text-transform:uppercase}
.situations{list-style:none;font-size:12.4px;line-height:1.45;font-weight:400;color:#555}
.situations li{position:relative;padding-left:18px;margin-bottom:9px}
.situations li::before{content:"";position:absolute;left:0;top:7px;width:5px;height:5px;border-top:1.5px solid #333;border-right:1.5px solid #333}
.situations b{color:#222;font-weight:600}
.hl{color:var(--green-bright);font-weight:600}
.step{position:absolute;background:var(--white);border-radius:4px;color:var(--green-dark);font-size:19px;line-height:1.2;padding:14px 18px 0 33px}
.step small{display:block;font-size:12px;line-height:1.35;color:#444;margin-top:6px}
.step-no{position:absolute;left:-10px;top:-12px}
.benefits{list-style:none;font-size:15.4px;line-height:1.55;font-weight:300;color:#333}
.benefits li{position:relative;padding-left:25px;margin-bottom:5px}
.benefits svg{position:absolute;left:0;top:6px}
.benefits .hl{font-weight:400}
.benefits u{text-underline-offset:2px}
.coach-name{font-size:26px;letter-spacing:2.5px;color:var(--green-bright);font-weight:400;line-height:1}
.coach-role{font-size:19px;letter-spacing:1.5px;color:var(--green-bright);font-weight:400;margin-top:4px}
.rule{height:3px;background:var(--green-dark)}
.contact-label{font-size:14.5px;font-weight:300;color:var(--green-bright)}
.contact-web{font-size:18.5px;font-weight:600;color:var(--green-dark)}
.contact-phone{font-size:24px;font-weight:600;color:var(--green-dark);letter-spacing:.5px}
</style>
</head>
<body>

<section class="page page--front">
  <svg class="abs" width="551" height="1200" viewBox="0 0 551 1200" style="left:0;top:0">
    <defs>
      <linearGradient id="gFront" x1="0" y1="0" x2="1" y2="1">
        <stop offset="0" stop-color="#46a53a"/><stop offset="1" stop-color="#37922f"/>
      </linearGradient>
    </defs>
    <rect width="551" height="900" fill="url(#gFront)"/>
    <rect x="0" y="467" width="551" height="122" fill="#ffffff"/>
    <polygon points="0,598 551,598 551,745 365,900 0,900" fill="#3f9e34"/>
    <polygon points="551,738 551,900 370,900" fill="var(--pale)"/>
  </svg>

  <div class="abs display headline" style="left:42px;top:58px">
    <div class="dark">Fahrangst</div>
    <div class="light">Erfolgreich</div>
    <div class="dark">Loswerden</div>
  </div>

  <div class="abs kicker" style="left:40px;top:272px">Wollen Sie:</div>
  <ul class="abs questions" style="left:0;top:300px;width:420px">
    <li><svg width="34" height="18" viewBox="0 0 34 18"><path d="M0 5h12l4 4-4 4H0z" fill="#fff"/><path d="M20 2l7 7-7 7" stroke="#fff" stroke-width="3" fill="none"/></svg>Fahrangst überwinden?</li>
    <li><svg width="34" height="18" viewBox="0 0 34 18"><path d="M0 5h12l4 4-4 4H0z" fill="#fff"/><path d="M20 2l7 7-7 7" stroke="#fff" stroke-width="3" fill="none"/></svg>Panikattacken beim Autofahren loswerden?</li>
    <li><svg width="34" height="18" viewBox="0 0 34 18"><path d="M0 5h12l4 4-4 4H0z" fill="#fff"/><path d="M20 2l7 7-7 7" stroke="#fff" stroke-width="3" fill="none"/></svg>Oder einfach sicher autofahren?</li>
  </ul>

  <svg class="abs" style="left:0;top:0" width="551" height="900" viewBox="0 0 551 900">
    <g role="img" aria-label="Foto: lächelnde junge Frau lehnt aus dem Autofenster und zeigt Daumen hoch">
      <defs>
        <linearGradient id="photoOne" x1="0" y1="0" x2="1" y2="1">
          <stop offset="0" stop-color="#c9d3d8"/><stop offset=".55" stop-color="#e7c7a8"/><stop offset="1" stop-color="#9aa3a8"/>
        </linearGradient>
      </defs>
      <polygon points="551,318 551,588 250,588" fill="url(#photoOne)"/>
    </g>
    <polygon points="551,306 551,318 250,588 236,588" fill="#ffffff"/>
  </svg>

  <div class="abs display callout" style="left:40px;top:490px">Dann sind Sie<br>hier richtig!</div>

  <svg class="abs" style="left:0;top:0" width="551" height="900" viewBox="0 0 551 900">
    <g role="img" aria-label="Foto: Frau mit grauen Haaren am Steuer eines Cabrios mit Lederpolstern">
      <defs>
        <linearGradient id="photoTwo" x1="0" y1="0" x2="1" y2="1">
          <stop offset="0" stop-color="#6e7772"/><stop offset=".5" stop-color="#c08a55"/><stop offset="1" stop-color="#2c3138"/>
        </linearGradient>
      </defs>
      <polygon points="228,598 551,598 551,738 370,892 0,892 0,783" fill="url(#photoTwo)"/>
    </g>
  </svg>

  <div class="abs situations-title" style="left:38px;top:926px">Kommt Ihnen eine dieser Situationen bekannt vor?</div>
  <ul class="abs situations" style="left:38px;top:966px;width:480px">
    <li><b>Angst oder Panikattacken</b> begleiten Sie <b>beim Autofahren</b>. Vielleicht vermeiden Sie deshalb das Autofahren komplett. - Sie möchten <span class="hl">angstfrei und/oder ohne Panikattacken fahren.</span></li>
    <li>Sie <b>trauen sich das Autofahren nicht (mehr) zu.</b> - Sie wünschen sich, <span class="hl">sicher, entspannt und stressfrei Auto zu fahren.</span></li>
    <li><b>Autofahren</b> erleben Sie unter <b>hoher Anspannung und Stress</b>. - Sie wünschen sich, Autofahren <span class="hl">sicher und entspannt</span> zu erleben.</li>
    <li>Bestimmte Situationen (z.B. <b>Autobahn, Baustellen, Stadtverkehr…</b>) bereiten Ihnen <b>großen Stress</b>. - Sie möchten diese Situationen <span class="hl">souveräner</span> meistern.</li>
  </ul>
</section>

<section class="page page--back">
  <svg class="abs" width="549" height="604" viewBox="0 0 549 604" style="left:0;top:0">
    <defs>
      <linearGradient id="gBack" x1="0" y1="0" x2="1" y2="1">
        <stop offset="0" stop-color="#46a53a"/><stop offset="1" stop-color="#37922f"/>
      </linearGradient>
      <linearGradient id="photoThree" x1="0" y1="0" x2="1" y2="1">
        <stop offset="0" stop-color="#9fc6e0"/><stop offset=".5" stop-color="#e9d43a"/><stop offset="1" stop-color="#8a8a5a"/>
      </linearGradient>
    </defs>
    <rect width="549" height="595" fill="url(#gBack)"/>
    <polygon points="549,302 549,314 236,595 222,595" fill="#ffffff"/>
    <g role="img" aria-label="Foto: gelber Kleinwagen mit Koffern auf dem Dach, fröhliche Fahrerin winkt aus dem Fenster">
      <polygon points="549,314 549,595 236,595" fill="url(#photoThree)"/>
    </g>
  </svg>

  <div class="abs display headline" style="left:40px;top:56px;font-size:70px">
    <div class="dark">Das muss nicht</div>
    <div class="light">so bleiben!</div>
  </div>

  <div class="abs kicker" style="left:40px;top:198px;font-size:20px">3 Schritte zur Lösung:</div>

  <div class="step" style="left:36px;top:245px;width:300px;height:53px">
    <svg class="step-no" width="70" height="60" viewBox="0 0 70 60"><polygon points="0,0 70,0 20,60 0,60" fill="#0f3b24"/><text x="16" y="32" font-family="Oswald,sans-serif" font-weight="700" font-size="24" fill="#fff">1</text></svg>
    Erstgespräch vereinbaren
  </div>
  <div class="step" style="left:36px;top:320px;width:382px;height:70px">
    <svg class="step-no" width="70" height="60" viewBox="0 0 70 60"><polygon points="0,0 70,0 20,60 0,60" fill="#0f3b24"/><text x="16" y="32" font-family="Oswald,sans-serif" font-weight="700" font-size="24" fill="#fff">2</text></svg>
    Analyse Ihrer individuellen Situation und Zielsetzung
  </div>
  <div class="step" style="left:36px;top:413px;width:300px;height:140px">
    <svg class="step-no" width="70" height="60" viewBox="0 0 70 60"><polygon points="0,0 70,0 20,60 0,60" fill="#0f3b24"/><text x="16" y="32" font-family="Oswald,sans-serif" font-weight="700" font-size="24" fill="#fff">3</text></svg>
    Individuelles Coaching und Training
    <small>(ggf. Fahrangst-Therapie - als psychotherapeutische Heilpraktikerin bin ich auf Angst- und Panikstörungen spezialisiert)</small>
  </div>

  <ul class="abs benefits" style="left:36px;top:643px;width:490px">
    <li><svg width="13" height="11" viewBox="0 0 13 11"><path d="M1 6l4 4 7-9" stroke="#333" stroke-width="1.6" fill="none"/></svg>über 10 Jahre Erfahrung als <span class="hl">Trainerin</span> und Coach im Bereich <span class="hl">Fahrsicherheit.</span></li>
    <li><svg width="13" height="11" viewBox="0 0 13 11"><path d="M1 6l4 4 7-9" stroke="#333" stroke-width="1.6" fill="none"/></svg>Als <span class="hl">psychotherapeutische Heilpraktikerin</span> bin ich <span class="hl">auf Angststörungen und Panikattacken spezialisiert</span></li>
    <li><svg width="13" height="11" viewBox="0 0 13 11"><path d="M1 6l4 4 7-9" stroke="#333" stroke-width="1.6" fill="none"/></svg><span class="hl">100 % auf Sie zugeschnitten:</span> ich hole Sie genau dort ab, wo Sie jetzt stehen und unterstütze Sie in <span class="hl">Ihrem Prozess individuell und zielführend.</span></li>
    <li><svg width="13" height="11" viewBox="0 0 13 11"><path d="M1 6l4 4 7-9" stroke="#333" stroke-width="1.6" fill="none"/></svg>Wenn es Ihnen nicht möglich ist, in meine Praxis nach Lindenfeld Nord zu kommen: <span class="hl"><u>Mit der mobilen</u> Praxis komme ich auch zu Ihnen.</span></li>
    <li><svg width="13" height="11" viewBox="0 0 13 11"><path d="M1 6l4 4 7-9" stroke="#333" stroke-width="1.6" fill="none"/></svg><span class="hl">Termine</span> sind auch <span class="hl">abends und am Wochenende möglich.</span></li>
  </ul>

  <div class="abs" role="img" aria-label="Porträtfoto der Trainerin in weißer Bluse" style="left:370px;top:945px;width:179px;height:255px;background:radial-gradient(ellipse at 55% 30%,#c9b3a0 0,#d9d2c8 30%,#f1f3ee 65%,rgba(241,243,238,0) 80%)"></div>

  <div class="abs" style="left:36px;top:980px">
    <div class="coach-name">Katrin Albrecht</div>
    <div class="coach-role">Fahrangst-Bewältigungs-Coach</div>
  </div>
  <div class="abs rule" style="left:36px;top:1038px;width:338px"></div>

  <div class="abs" style="left:36px;top:1062px">
    <div class="contact-label">Weitere Informationen finden Sie auf:</div>
    <div class="contact-web">www.fahrsicher-coaching-beispiel.de</div>
    <div class="contact-label" style="margin-top:12px">Oder rufen Sie mich einfach an:</div>
    <div class="contact-phone">0151 00 12 34 56</div>
  </div>
</section>

</body>
</html>
```